Harrowgate Estates Business Card for Apartment Buildings

Create business cards for resident managers who run apartment buildings. The audience is the public who are searching for apartment rentals, and current residents who live at the apartment building. Key design element will be incorporating the company logo, however, the logo cannot dominate. The building name and manager name are more important than the logo. Current business card design leaves little room for copy, so we may need to reduce the size on the current card to allow for more space for copy.

Target Market(s)

Adults 18-65 years of age, who are looking for an apartment rental, plus current residents who live at our apartment buildings.

Industry/Entity Type

Property Management

Contact Information for Business Card

A major design element will be use of the company logo. Important property and manager contact information must be part of the design. The size of the logo will need to be reduced to make room for building and manager contact copy.

Font styles to use
Sans Serif

Colors
3176b5
000000
959595
ffffff

Requirements
Must have
• 1) Incorporate the company logo.
• 2) Use the company colors (dark blue, black/grey, over white).
• 3) FEATURE THE BUILDING NAME
• 4) FEATURE THE MANAGER NAME
• 5) The company name is less important than BUILDING and MANAGER
• 6) Manager contact information
• **SEE ATTACHED CREATIVE BRIEF**
Nice to have
• 1) Back of card logo watermark
• 2) Ability to write notes on back of carfd
Should not have
• Avoid letting the company logo dominate the card, the building name and manager are more important than the company logo.

```html
<!DOCTYPE html>
<html lang="en">
<head>
<meta charset="utf-8">
<title>Harrowgate Estates – Resident Manager Cards</title>
<link href="https://fonts.googleapis.com/css2?family=Roboto:wght@400;500;700&family=Roboto+Condensed:wght@700&display=swap" rel="stylesheet">
<style>
  :root {
    --brand-blue: #0a69a8;
    --line-blue: #2f74b3;
    --charcoal: #474749;
    --ink: #3a3a3c;
    --paper: #ffffff;
    --backdrop: #e9e9e9;
    --rule-light: #d8d8d8;
  }
  * { margin: 0; padding: 0; box-sizing: border-box; }
  html, body {
    width: 1200px; height: 900px; overflow: hidden;
    background: var(--backdrop);
    font-family: "Roboto", Arial, sans-serif;
  }
  .sheet { position: relative; width: 1200px; height: 900px; }

  .card {
    position: absolute;
    width: 500px; height: 292px;
    background: var(--paper);
    overflow: hidden;
  }
  .card--front-top { left: 93px; top: 94px; }
  .card--back-light { left: 616px; top: 94px; }
  .card--front-bottom { left: 93px; top: 478px; }
  .card--back-dark { left: 616px; top: 478px; background: var(--charcoal); }

  /* front */
  .brand-panel {
    position: absolute; left: 0; top: 0;
    width: 174px; height: 100%;
    background: var(--brand-blue);
  }
  .brand-panel__mark {
    position: absolute; left: 57px; top: 116px;
    width: 60px; height: 60px;
    background: var(--paper);
  }
  .front-copy {
    position: absolute; right: 23px; top: 34px;
    text-align: right;
    color: var(--ink);
  }
  .company-name {
    font-weight: 700;
    font-size: 25px;
    line-height: 1;
    color: var(--brand-blue);
    letter-spacing: 0.5px;
    margin-bottom: 22px;
  }
  .manager-name {
    font-family: "Roboto Condensed", "Arial Narrow", sans-serif;
    font-weight: 700;
    font-size: 19px;
    line-height: 1.1;
    color: var(--brand-blue);
  }
  .manager-title {
    font-size: 13.5px;
    line-height: 1.3;
    margin-bottom: 8px;
  }
  .property-address, .contact-list {
    font-size: 12px;
    line-height: 15px;
    font-style: normal;
  }
  .property-name { font-weight: 500; }
  .contact-list { margin-top: 9px; list-style: none; }

  /* back */
  .notes-label {
    position: absolute; left: 45px; top: 35px;
    font-size: 15px;
    color: var(--line-blue);
  }
  .card--back-dark .notes-label { color: var(--paper); }
  .notes-lines {
    position: absolute; left: 45px; top: 77px;
    width: 413px; list-style: none;
  }
  .notes-lines li {
    height: 27px;
    border-top: 1px solid var(--line-blue);
  }
  .card--back-dark .notes-lines li { border-top-color: var(--rule-light); }
</style>
</head>
<body>
<main class="sheet">

  <section class="card card--front-top" aria-label="Business card front">
    <div class="brand-panel"><span class="brand-panel__mark"></span></div>
    <div class="front-copy">
      <p class="company-name">HARROWGATE ESTATES</p>
      <h2 class="manager-name">MARISOL DELGADO</h2>
      <p class="manager-title">Resident Manager</p>
      <address class="property-address">
        <span class="property-name">Cedar Court Apartments</span><br>
        2481 Larkspur Avenue<br>
        Fairview, CA 92418
      </address>
      <ul class="contact-list">
        <li>Phone 555-214-3380</li>
        <li>Fax 555-214-3391</li>
        <li>Cell 555-808-4172</li>
        <li>marisol@harrowgateest.com</li>
        <li>www.harrowgateestates.com</li>
      </ul>
    </div>
  </section>

  <section class="card card--back-light" aria-label="Business card back, light">
    <p class="notes-label">Write Notes:</p>
    <ul class="notes-lines"><li></li><li></li><li></li><li></li><li></li><li></li><li></li></ul>
  </section>

  <section class="card card--front-bottom" aria-label="Business card front">
    <div class="brand-panel"><span class="brand-panel__mark"></span></div>
    <div class="front-copy">
      <p class="company-name">HARROWGATE ESTATES</p>
      <h2 class="manager-name">MARISOL DELGADO</h2>
      <p class="manager-title">Resident Manager</p>
      <address class="property-address">
        <span class="property-name">Cedar Court Apartments</span><br>
        2481 Larkspur Avenue<br>
        Fairview, CA 92418
      </address>
      <ul class="contact-list">
        <li>Phone 555-214-3380</li>
        <li>Fax 555-214-3391</li>
        <li>Cell 555-808-4172</li>
        <li>marisol@harrowgateest.com</li>
        <li>www.harrowgateestates.com</li>
      </ul>
    </div>
  </section>

  <section class="card card--back-dark" aria-label="Business card back, dark">
    <p class="notes-label">Write Notes:</p>
    <ul class="notes-lines"><li></li><li></li><li></li><li></li><li></li><li></li><li></li></ul>
  </section>

</main>
</body>
</html>
```